Natural Kelp product needs a new Label design

We supply premium quality 'Marlow Kelp' from the pristine waters of South Eastern Australia, for human consumption.  The company has been operating since 1965.
Kelp (seaweed) is a type of superfood and is used as a health supplement  - high in vitamins, minerals, fibre and iodine.
Many people benefit from kelp - however the target market is health food stores and their customers. The look should be organic/natural/simple clean and fresh. I have also thought about a retro 60's look as that was when the product was first established. There are currently two products - granules and powder and 2 sizes.
I have uploaded the current label, which was produced more than 10 years ago and needs updating.
The label will either be reproduced as stickers or printed directly onto the new packaging which will be food grade cardboard tubes such as those used for packaging tea. (see Quorixa for samples)
The word Kelp should be highlighted and perhaps larger than “Marlow”.
The company is called Tarrow Bay Products and I have uploaded a logo as well as the ‘embossed’ look and feel I like.

Target Market(s)
Health food stores, wellness industry, organic buyers
Industry/Entity Type
Health And Wellness
Requirements
Must have
- Tarrow Bay Product Logo, natural look and feel

Nice to have
- Embossed look, sand/sandpaper type background

```html
<!DOCTYPE html>
<html lang="en">
<head>
<meta charset="utf-8">
<title>Marlow Kelp meal – label range</title>
<link href="https://fonts.googleapis.com/css2?family=Philosopher:wght@400;700&display=swap" rel="stylesheet">
<style>
  :root {
    --backdrop: #f3f3f3;
    --kraft: #cfab87;
    --kraft-light: #d9b894;
    --ink: #2a1d15;
    --lid-cocoa: #4d3f35;
    --lid-gold: #e3bd45;
    --gold-line: #e8b520;
  }
  * { margin: 0; padding: 0; box-sizing: border-box; }
  html, body { width: 1200px; height: 1110px; overflow: hidden; }
  body { background: var(--backdrop); position: relative; }

  .tube { position: absolute; width: 340px; }
  .tube--tl { left: 151px; top: 60px; }
  .tube--tr { left: 688px; top: 60px; }
  .tube--bl { left: 155px; top: 633px; }
  .tube--br { left: 688px; top: 633px; }

  .lid { height: 110px; border-radius: 6px 6px 0 0; }
  .tube--bl .lid, .tube--br .lid { height: 67px; }
  .lid--cocoa { background: var(--lid-cocoa); }
  .lid--gold { background: linear-gradient(180deg, #f0cf63, var(--lid-gold) 60%, #d9ae35); }

  .label {
    position: relative;
    height: 300px;
    background: linear-gradient(90deg, var(--kraft) 0%, var(--kraft-light) 50%, var(--kraft) 100%);
    border-radius: 0 0 10px 10px;
    color: var(--ink);
    text-align: center;
    font-family: 'Philosopher', sans-serif;
  }
  .label__rule {
    position: absolute; left: 0; right: 0; top: 12px; height: 4px;
    background: var(--gold-line);
  }
  .label__claim {
    position: absolute; left: 0; right: 0; top: 27px;
    font-size: 16px; line-height: 1; letter-spacing: 0.3px;
  }
  .label__product {
    position: absolute; left: 0; right: 0; top: 72px;
    font-size: 40px; font-weight: 700; line-height: 1;
  }
  .label__form {
    position: absolute; left: 0; right: 0; top: 122px;
    font-size: 18px; font-weight: 400; line-height: 1; letter-spacing: 1px;
  }
  .brand__dot {
    position: absolute; left: 50%; top: 158px;
    width: 82px; height: 82px; margin-left: -41px;
    border-radius: 50%; background: var(--ink);
  }
  .brand__name {
    position: absolute; left: 0; right: 0; top: 256px;
    font-size: 21px; font-weight: 700; line-height: 1;
  }
</style>
</head>
<body>

<div class="tube tube--tl">
  <div class="lid lid--cocoa"></div>
  <div class="label">
    <div class="label__rule"></div>
    <p class="label__claim">Pure 100% Australian Sea Kelp</p>
    <p class="label__product">Marlow Kelp</p>
    <p class="label__form">meal</p>
    <span class="brand__dot"></span>
    <p class="brand__name">Tarrow Bay Products</p>
  </div>
</div>

<div class="tube tube--tr">
  <div class="lid lid--gold"></div>
  <div class="label">
    <div class="label__rule"></div>
    <p class="label__claim">Pure 100% Australian Sea Kelp</p>
    <p class="label__product">Marlow Kelp</p>
    <p class="label__form">meal</p>
    <span class="brand__dot"></span>
    <p class="brand__name">Tarrow Bay Products</p>
  </div>
</div>

<div class="tube tube--bl">
  <div class="lid lid--cocoa"></div>
  <div class="label">
    <div class="label__rule"></div>
    <p class="label__claim">Pure 100% Australian Sea Kelp</p>
    <p class="label__product">Marlow Kelp</p>
    <p class="label__form">meal</p>
    <span class="brand__dot"></span>
    <p class="brand__name">Tarrow Bay Products</p>
  </div>
</div>

<div class="tube tube--br">
  <div class="lid lid--gold"></div>
  <div class="label">
    <div class="label__rule"></div>
    <p class="label__claim">Pure 100% Australian Sea Kelp</p>
    <p class="label__product">Marlow Kelp</p>
    <p class="label__form">meal</p>
    <span class="brand__dot"></span>
    <p class="brand__name">Tarrow Bay Products</p>
  </div>
</div>

</body>
</html>
```